Willow of Meadow Uniform Label Redesign

To refine our current product label designs into one, simple, modern, crisp, general look that can be adapted to all our all Natural Skin Care and Wellness products. I am inspired by the elegant versatility of products like Lumavel Botanic Beauty or Tarn Beauty label schemes. We no longer want labels that indicate scent or ingredients. We have two primary colors that we want to maintain (#096CA3 and #DEE33F), and are willing to entertain subtle additions of others, other than black. Our labels will be printed on white or clear material. We use mainly Cosmo or Boston Round container shapes, plus flat top, smooth, round jars. Maybe a faded watermark highlight the "natural" or "beautiful" side of our products. we need to convey confidence, while remaining simple. We currently use the Advantage font. Maybe Century Gothic may work. Something similar that is easy on the eyes. Maybe vertical main text? We are willing to entertain a lot of ideas. These designs will offer ideas into our eventual Website (www.willowofmeadow-example.com) redesign.

Target Market(s)

Those who are familiar with the power of natural, plant based skin care and wellness products

Industry/Entity Type

Natural Skin Care and Wellness

Font styles to use
Sans Serif
Other font styles liked:
• Century Gothic, Advantage, or similar that is easy on the eyes

Colors
0054AA
0677BA
7BADD7
CADEEF
E8F1F8
59FF00
82FF00
B8FF75
E3FFCB
F4FFEA

Requirements
Must have
• "Clean Lines"; These colors: (#096CA3 and #DEE33F)
Nice to have
• MAYBE vertical main text or a watermark image

```html
<!DOCTYPE html>
<html lang="en">
<head>
<meta charset="utf-8">
<title>Willow of Meadow – Jar Label</title>
<link rel="stylesheet" href="https://fonts.googleapis.com/css2?family=Questrial&display=swap">
<style>
  :root {
    --brand-blue: #096CA3;
    --brand-lime: #DEE33F;
    --label-white: #F5F7F9;
    --page-bg: #FFFFFF;
  }
  html, body {
    margin: 0;
    padding: 0;
    width: 1200px;
    height: 1199px;
    overflow: hidden;
    background: var(--page-bg);
  }
  .canvas {
    position: relative;
    width: 1200px;
    height: 1199px;
  }
  .label {
    position: absolute;
    left: 60px;
    top: 260px;
    width: 1080px;
    height: 680px;
    background: var(--label-white);
    overflow: hidden;
  }
  .pattern-band {
    position: absolute;
    top: 0;
    width: 150px;
    height: 100%;
    opacity: 0.85;
  }
  .pattern-band--left {
    left: 0;
    background: linear-gradient(to right, var(--brand-lime) 0%, rgba(222,227,63,0.35) 60%, rgba(222,227,63,0) 100%);
  }
  .pattern-band--right {
    right: 0;
    background: linear-gradient(to left, var(--brand-lime) 0%, rgba(222,227,63,0.35) 60%, rgba(222,227,63,0) 100%);
  }
  .brand-block {
    position: absolute;
    left: 0;
    right: 0;
    top: 150px;
    display: flex;
    flex-direction: column;
    align-items: center;
    font-family: "Questrial", sans-serif;
  }
  .brand-mark {
    width: 150px;
    height: 150px;
    display: block;
  }
  .brand-name {
    margin: 48px 0 0;
    font-size: 56px;
    font-weight: 400;
    color: var(--brand-blue);
    letter-spacing: 0.5px;
  }
  .product-name {
    margin: 56px 0 0;
    font-size: 62px;
    font-weight: 400;
    color: var(--brand-lime);
  }
</style>
</head>
<body>
  <main class="canvas">
    <section class="label">
      <div class="pattern-band pattern-band--left" role="img" aria-label="Lime halftone dot pattern fading toward the centre"></div>
      <div class="pattern-band pattern-band--right" role="img" aria-label="Lime halftone dot pattern fading toward the centre"></div>
      <div class="brand-block">
        <svg class="brand-mark" viewBox="0 0 150 150" aria-hidden="true">
          <circle cx="75" cy="75" r="70" fill="none" stroke="var(--brand-blue)" stroke-width="4"/>
        </svg>
        <h1 class="brand-name">Willow of Meadow</h1>
        <p class="product-name">Product name</p>
      </div>
    </section>
  </main>
</body>
</html>
```